BrambleWorks business card

Looking for business card design that supports our company/software values. We have 2 logo designs at the moment but open to change if you think you can enhance the brand. Check out website www.brambleworks.com.au.

Target Market(s)

Education

Contact Information for Business Card

Name, title, mobile, email and website

Font styles to use
Sans Serif

Colors

Designer to choose colors to be used in the design.

Requirements
Must have
• BrambleWorks logo with tree and tagline on rear side with dark grey background colour

```html
<!DOCTYPE html>
<html lang="en">
<head>
<meta charset="utf-8">
<title>BrambleWorks business card</title>
<link rel="stylesheet" href="https://fonts.googleapis.com/css2?family=Carlito&family=Ubuntu:wght@400;500&display=swap">
<style>
  :root {
    --slate: #3b4a47;
    --paper: #ffffff;
    --ink: #2f3533;
    --frame: #8a8f8d;
    --leaf: #6aa336;
    --dots: #9a9e9c;
  }
  * { margin: 0; padding: 0; box-sizing: border-box; }
  html, body { width: 1200px; height: 347px; overflow: hidden; background: var(--paper); }
  .sheet { position: relative; width: 1200px; height: 347px; }

  .card-back {
    position: absolute; left: 0; top: 0; width: 580px; height: 347px;
    background: var(--slate);
  }
  .badge {
    position: absolute; left: 183px; top: 108px; width: 183px; height: 134px;
    background: var(--paper);
  }
  .badge-frame {
    position: absolute; left: 6px; top: 6px; right: 6px; bottom: 6px;
    border: 1px solid var(--frame);
    display: flex; flex-direction: column; align-items: center; justify-content: center;
    gap: 8px;
  }

  .wordmark {
    display: flex; align-items: center; gap: 6px;
    font-family: "Ubuntu", sans-serif; font-weight: 500; color: var(--slate);
  }
  .wordmark-dot { width: 9px; height: 9px; border-radius: 50%; background: var(--leaf); }
  .badge .wordmark { font-size: 21px; }
  .tagline {
    font-family: "Ubuntu", sans-serif; font-weight: 400; color: var(--ink);
    font-size: 10.5px;
  }

  .card-front { position: absolute; left: 580px; top: 0; width: 620px; height: 347px; }
  .front-brand {
    position: absolute; left: 160px; top: 128px; width: 150px;
    display: flex; flex-direction: column; align-items: center; gap: 8px;
  }
  .front-brand .wordmark { font-size: 21px; }
  .divider {
    position: absolute; left: 326px; top: 115px; height: 97px;
    border-left: 1.5px dotted var(--dots);
  }
  .person { position: absolute; left: 345px; top: 112px; font-family: "Carlito", sans-serif; color: #111; }
  .person-name { font-size: 20.5px; line-height: 1.2; }
  .person-role { font-size: 12.5px; margin-top: 1px; }
  .person-contact { font-size: 13.5px; line-height: 18px; margin-top: 20px; }

  .company-info {
    position: absolute; left: 192px; width: 350px; top: 282px;
    text-align: center; font-family: "Ubuntu", sans-serif; font-size: 11px;
    line-height: 15.5px; color: var(--ink);
  }
</style>
</head>
<body>
<div class="sheet">
  <section class="card-back">
    <div class="badge">
      <div class="badge-frame">
        <div class="wordmark"><span class="wordmark-dot"></span>BrambleWorks</div>
        <div class="tagline">Student Success Platform</div>
      </div>
    </div>
  </section>

  <section class="card-front">
    <div class="front-brand">
      <div class="wordmark"><span class="wordmark-dot"></span>BrambleWorks</div>
      <div class="tagline">Student Success Platform</div>
    </div>
    <div class="divider"></div>
    <div class="person">
      <div class="person-name">Name Surname</div>
      <div class="person-role">Designation</div>
      <div class="person-contact">+61-0000 0000<br>info@email.com</div>
    </div>
    <div class="company-info">
      www.brambleworks.com.au<br>
      Phone: +61 00 000 000 &nbsp;|&nbsp; Fax: +61 00 000 000<br>
      Building name, City name, Street name, State, Zip code, Australia
    </div>
  </section>
</div>
</body>
</html>
```